BrightPlacely.com Wordpress Theme

Hi,

I am looking for a new theme for my wordpress site. The site looks average at the moment and needs a boost. I want to have a better user experience for publishers and advertisers and the proposition for each needs to be clear with better links to registration for both.

Publisher and Advertiser sign up buttons should be on the home page.

I am leaving the brief open save I request that you use green colours on the template.

I want room to be able to add more tabs on the top level if we introduce a blog or other services.

The layout needs to be solid and please work with the copy that's already there.

see http://brightplacely.example

I am looking forward to reviewing your ideas and designs.
Updates

The button to carbon neutral cert I am going to want to make smaller and put it in the bottom of the site.

Do not go down the too fluffy green route with windmills and fuzzy clouds. I am looking for something simple, professional but also organic with a bit of zest to it. 

We are not a niche player serving ads to green only site with green only ads. We simply neutralise the effect of online advertising campaigns.

Some decent images in the header on rotation could work I am not sure. I think these would have to be abstract and largely if not totally green in colour.

Target Market(s)

BrightPlacely.com is an online ad network. Our targets are publishers and advertisers. We bring them together through providing ad serving to the network we have built on behalf of our advertisers.

Advertisers are agencys, brands, large companies looking to sell online or create awareness of the brand.

Requirements
Must have
• Please keep the site clean and use green and white
• Call to action to both publishers and advertisers to join (buttons on home page)

```html
<!DOCTYPE html>
<html lang="en">
<head>
<meta charset="utf-8">
<title>BrightPlacely.com</title>
<link rel="stylesheet" href="https://fonts.googleapis.com/css2?family=Arimo:wght@400;700&display=swap">
<style>
:root{
  --green:#3d9a3f;
  --green-dark:#1e6a1a;
  --green-text:#3a9a36;
  --band-top:#8cc35f;
  --band-bottom:#5e9e3f;
  --grey-text:#555;
  --body-text:#333;
  --hero-bg:#f4f5f1;
  --white:#fff;
}
*{box-sizing:border-box;margin:0;padding:0}
html,body{width:1200px;height:1071px;overflow:hidden}
body{font-family:"Arimo",Arial,sans-serif;background:var(--white);color:var(--body-text);position:relative}
a{text-decoration:none;color:inherit}

.site-header{position:absolute;left:0;top:0;width:1200px;height:104px;background:var(--white);border-bottom:1px solid #d8dbd4}
.brand{position:absolute;left:88px;top:28px;display:flex;align-items:center;gap:10px;font-size:38px;font-weight:700;color:var(--green-dark);letter-spacing:-0.5px}
.brand-dot{width:30px;height:30px;border-radius:50%;background:var(--green)}
.main-nav{position:absolute;right:108px;top:42px;display:flex;align-items:center;font-size:13.5px;color:var(--green)}
.main-nav a{padding:0 7px}
.main-nav .sep{color:#ccc}
.main-nav .current{background:#74b34c;color:var(--white);border-radius:11px;padding:3px 17px;margin-right:2px}

.hero{position:absolute;left:0;top:105px;width:1200px;height:397px;background:linear-gradient(#f6f7f3 0,#f3f4ef 290px,#e3e4e1 320px,#f3f3f1 397px);border-bottom:2px solid #9a9a9a}
.hero-title{position:absolute;left:88px;top:18px;font-size:30px;line-height:31px;font-weight:700;color:var(--green)}
.hero-intro{position:absolute;left:88px;top:94px;width:511px;font-size:14.4px;line-height:16.5px;text-align:justify;color:#111}
.features{position:absolute;top:178px;list-style:none;font-size:14.5px;line-height:15px;color:var(--green-text)}
.features li{display:flex;gap:6px;margin-bottom:9px}
.features svg{flex:none;width:14px;height:14px;margin-top:1px}
.features.left{left:88px;width:340px}
.features.right{left:438px;width:180px}
.cta-start{position:absolute;left:88px;top:330px;width:155px;height:51px;border-radius:4px;background:linear-gradient(#68b03e,#2a8a1d 55%,#136c0f);box-shadow:inset 0 0 0 2px #8fcf5e;color:var(--white);font-size:20px;font-weight:700;display:flex;align-items:center;padding-left:15px;gap:8px}
.hero-art{position:absolute;left:635px;top:-22px;width:490px;height:417px;background:radial-gradient(ellipse at 70% 30%,#8fcf6e 0,#dfe8dc 40%,rgba(240,242,238,0) 72%)}

.audience-band{position:absolute;left:0;top:503px;width:1200px;height:141px;background:linear-gradient(var(--band-top),var(--band-bottom));border-bottom:1px solid #4a7d30}
.audience-card{position:absolute;top:15px;width:489px;height:113px;border-radius:9px;background:linear-gradient(rgba(255,255,255,.28),rgba(255,255,255,.04));color:var(--white)}
.audience-card.advertisers{left:90px}
.audience-card.publishers{left:601px}
.audience-icon{position:absolute;left:18px;top:15px;width:82px;height:82px;border-radius:50%;background:var(--white);box-shadow:0 0 0 3px rgba(255,255,255,.4);display:flex;align-items:center;justify-content:center}
.audience-body{position:absolute;left:118px;top:12px;width:360px}
.audience-body h2{font-size:14.5px;font-weight:700;margin-bottom:2px}
.audience-body p{font-size:12.5px;line-height:14px}
.audience-actions{position:absolute;left:118px;top:84px;display:flex;gap:4px}
.pill{background:var(--white);color:var(--green-dark);font-size:13px;border-radius:11px;padding:3px 12px}

.info-columns{position:absolute;left:0;top:644px;width:1200px;height:226px}
.info-col{position:absolute;top:30px;width:316px}
.info-col h3{font-size:14.5px;font-weight:700;color:var(--grey-text);padding-bottom:10px;border-bottom:1px dotted #bbb;margin-bottom:11px}
.info-col p{font-size:12.6px;line-height:18px;color:#444}
.info-col .more{color:var(--green)}
.col-referral{left:88px;top:28px}
.col-news{left:424px}
.col-blog{left:761px;width:316px}
.blog-post{margin-bottom:8px;font-size:12.6px;line-height:16px}
.blog-post a{color:var(--green)}
.btn-soft{display:inline-block;margin-top:8px;margin-left:-3px;padding:2px 11px;border-radius:11px;background:linear-gradient(#f5f5f5,#d9d9d9);color:#888;font-size:12.6px}

.site-footer{position:absolute;left:0;top:870px;width:1200px;height:201px;background:linear-gradient(#dcdcdc,#f3f3f3 45%,#fff);border-top:3px solid #f0f0f0}
.foot-col{position:absolute;top:18px;font-size:12.6px;line-height:19px;color:#444}
.foot-col h4{font-size:13px;font-weight:700;color:var(--grey-text);margin-bottom:-1px}
.foot-col ul{list-style:none}
.foot-about{position:absolute;left:784px;top:16px;width:306px;font-size:12.6px;line-height:18px;color:#444}
.foot-about h4{font-size:13px;color:var(--green);margin-bottom:5px}
.foot-rule{position:absolute;left:88px;top:124px;width:1006px;border-top:1px solid #bbb}
.badge{position:absolute;left:88px;top:135px;width:112px;height:48px;border-radius:6px;background:#d7e8cf}
.phones{position:absolute;left:218px;top:150px;font-size:14.5px;color:var(--green-dark)}
.phones b{font-weight:700}
</style>
</head>
<body>

<header class="site-header">
  <a class="brand" href="http://brightplacely.example"><span class="brand-dot"></span>BrightPlacely.com</a>
  <nav class="main-nav">
    <a class="current" href="#">Home</a>
    <a href="#">Advertisers</a><span class="sep">|</span>
    <a href="#">Publishers</a><span class="sep">|</span>
    <a href="#">Referral</a><span class="sep">|</span>
    <a href="#">Offsetting</a><span class="sep">|</span>
    <a href="#">Contact</a>
  </nav>
</header>

<section class="hero">
  <div class="hero-art" role="img" aria-label="Laptop surrounded by a swarm of pointing-hand cursors"></div>
  <h1 class="hero-title">Neutralizing environment<br>impact of your campaign</h1>
  <p class="hero-intro">BrightPlacely.com is a contextual advertising network and ad exchange that brings together publishers of high quality content with advertisers, enabling them to reach their target market whilst publishers monetize their sites through advertising that's in keeping with their sites.</p>
  <ul class="features left">
    <li><svg viewBox="0 0 14 14"><rect x="1" y="1" width="12" height="12" rx="2" fill="none" stroke="#3d9a3f" stroke-width="2"/><path d="M3.5 7l2.5 2.5L12 2" fill="none" stroke="#3d9a3f" stroke-width="2.2"/></svg>Hundreds of millions of monthly ad impressions across ours and our partner networks</li>
    <li><svg viewBox="0 0 14 14"><rect x="1" y="1" width="12" height="12" rx="2" fill="none" stroke="#3d9a3f" stroke-width="2"/><path d="M3.5 7l2.5 2.5L12 2" fill="none" stroke="#3d9a3f" stroke-width="2.2"/></svg>170+ content channels to target</li>
    <li><svg viewBox="0 0 14 14"><rect x="1" y="1" width="12" height="12" rx="2" fill="none" stroke="#3d9a3f" stroke-width="2"/><path d="M3.5 7l2.5 2.5L12 2" fill="none" stroke="#3d9a3f" stroke-width="2.2"/></svg>B2B &amp; B2C traffic</li>
    <li><svg viewBox="0 0 14 14"><rect x="1" y="1" width="12" height="12" rx="2" fill="none" stroke="#3d9a3f" stroke-width="2"/><path d="M3.5 7l2.5 2.5L12 2" fill="none" stroke="#3d9a3f" stroke-width="2.2"/></svg>Geo Targeting</li>
  </ul>
  <ul class="features right">
    <li><svg viewBox="0 0 14 14"><rect x="1" y="1" width="12" height="12" rx="2" fill="none" stroke="#3d9a3f" stroke-width="2"/><path d="M3.5 7l2.5 2.5L12 2" fill="none" stroke="#3d9a3f" stroke-width="2.2"/></svg>Behavioural Targeting</li>
    <li><svg viewBox="0 0 14 14"><rect x="1" y="1" width="12" height="12" rx="2" fill="none" stroke="#3d9a3f" stroke-width="2"/><path d="M3.5 7l2.5 2.5L12 2" fill="none" stroke="#3d9a3f" stroke-width="2.2"/></svg>Re-Targeting</li>
    <li><svg viewBox="0 0 14 14"><rect x="1" y="1" width="12" height="12" rx="2" fill="none" stroke="#3d9a3f" stroke-width="2"/><path d="M3.5 7l2.5 2.5L12 2" fill="none" stroke="#3d9a3f" stroke-width="2.2"/></svg>Real Time Campaign Tracking &amp; Reporting</li>
    <li><svg viewBox="0 0 14 14"><rect x="1" y="1" width="12" height="12" rx="2" fill="none" stroke="#3d9a3f" stroke-width="2"/><path d="M3.5 7l2.5 2.5L12 2" fill="none" stroke="#3d9a3f" stroke-width="2.2"/></svg>ROI tracking</li>
  </ul>
  <a class="cta-start" href="#">Get Started <svg width="12" height="18" viewBox="0 0 12 18"><path d="M1 1l10 8-10 8z" fill="#fff"/></svg></a>
</section>

<section class="audience-band">
  <div class="audience-card advertisers">
    <div class="audience-icon"><svg width="46" height="44" viewBox="0 0 46 44"><rect x="2" y="2" width="42" height="30" rx="2" fill="#5e9e3f"/><rect x="8" y="8" width="30" height="18" fill="#fff"/><rect x="19" y="32" width="8" height="6" fill="#5e9e3f"/><rect x="10" y="38" width="26" height="4" fill="#5e9e3f"/></svg></div>
    <div class="audience-body"><h2>Advertisers</h2><p>BrightPlacely.com can provide you access to over a billion impressions a month to drive quality traffic to your website to convert.</p></div>
    <div class="audience-actions"><a class="pill" href="#">Register</a><a class="pill" href="#">Read more</a></div>
  </div>
  <div class="audience-card publishers">
    <div class="audience-icon"><svg width="60" height="48" viewBox="0 0 60 48"><circle cx="13" cy="14" r="7" fill="#5e9e3f"/><circle cx="47" cy="14" r="7" fill="#5e9e3f"/><circle cx="30" cy="11" r="9" fill="#5e9e3f"/><path d="M0 46c0-14 6-20 13-20s13 6 13 20zM34 46c0-14 6-20 13-20s13 6 13 20z" fill="#5e9e3f"/><path d="M12 48c0-18 8-25 18-25s18 7 18 25z" fill="#5e9e3f" stroke="#fff" stroke-width="2"/></svg></div>
    <div class="audience-body"><h2>Publishers</h2><p>We are always on the look out for new publishers to join our ad network and by joining us you are joining a network of aggregated content.</p></div>
    <div class="audience-actions"><a class="pill" href="#">Register</a><a class="pill" href="#">Read more</a></div>
  </div>
</section>

<section class="info-columns">
  <div class="info-col col-referral">
    <h3>Referral Program</h3>
    <p>As a referral partner, you can place one of our text links and/or banners on your website to direct visitors to BrightPlacely.com. You start generating income when a user clicks on your text link or banner and registers as a BrightPlacely.com advertiser or publisher.</p>
    <a class="btn-soft" href="#">read more</a>
  </div>
  <div class="info-col col-news">
    <h3>Latest News</h3>
    <p>Lorem ipsum dolor sit amet, consectetur adipiscing elit. Proin sodales, urna ut mattis ullamcorper, dolor velit dictum lacus, a fringilla orci sapien <a class="more" href="#">Read more »</a></p>
    <p style="margin-top:14px">Pellentesque vehicula vehicula nisi a mattis. Praesent iaculis, mauris quis aliquet pretium, turpis nisl fermen-tum dolor, a consectetur odio urna. <a class="more" href="#">Read more »</a></p>
  </div>
  <div class="info-col col-blog">
    <h3>From Our Blog</h3>
    <div class="blog-post"><a href="#">4 reasons why people choose to share content online</a><br>August 26th, 2010 by Nora Whitfield</div>
    <div class="blog-post"><a href="#">The kittens are coming to Bristol!</a><br>August 24th, 2010 by Clara Dunmore</div>
    <div class="blog-post"><a href="#">Blogger tips: How to write compelling blog posts</a><br>August 24th, 2010 by Owen Ashgrove</div>
  </div>
</section>

<footer class="site-footer">
  <div class="foot-col" style="left:88px"><h4>Pages</h4><ul><li>Contact</li><li>Offsetting</li><li>Referral</li></ul></div>
  <div class="foot-col" style="left:229px"><h4>Publishers</h4><ul><li>Advertising Formats</li><li>Publisher Information</li><li>Publisher Login</li><li>Publisher Sign Up</li></ul></div>
  <div class="foot-col" style="left:399px"><h4>Advertisers</h4><ul><li>Advertiser Information</li><li>Advertiser Login</li><li>Advertiser Sign Up</li><li>Advertising Formats</li></ul></div>
  <div class="foot-col" style="left:566px"><h4>Useful Info</h4><ul><li>Terms &amp; Conditions : Advertisers</li><li>Terms &amp; Conditions : Publishers</li><li>User Guide: Advertisers</li><li>User Guide: Publishers</li></ul></div>
  <div class="foot-about"><h4>Copyright BrightPlacely.com Ltd 2010</h4><p>BrightPlacely.com offers publishers to the opportunity to earn more income through text (inline text links) or by displaying targeted contextual advertising banner ads on their websites or blogs.</p></div>
  <div class="foot-rule"></div>
  <div class="badge" role="img" aria-label="Carbon neutral website badge"></div>
  <p class="phones">555 010-4821 <b>USA</b> &nbsp;| &nbsp;020 7946 0123 <b>UK</b> &nbsp;| &nbsp;08-555 10 203 <b>Sweden</b> &nbsp;| &nbsp;02 5550 1842 <b>Australia</b> &nbsp;| &nbsp;21 5550172 <b>Hungary</b></p>
</footer>

</body>
</html>
```